business card for LWR pty ltd

We require a business card that stands out . I have included our company flyer and would like the services listed to be put on the card so when we Give out the cards to customers they have an idea of services we provide. need the winning design to be in editable photo shop format, editable iMac pages format or editable windows publisher format, so that I can enter in names, email addresses, phone numbers etc myself. I have included a pdf documents of info / items needed on the card to use as reference please.
Updates

need more submissions

Need extra days to review

Sick

Target Market(s)

new customers

Contact Information for Business Card

details are on attached business card requirements file

Requirements
Must have
• I have attached a list of must haves

```html
<!DOCTYPE html>
<html lang="en">
<head>
<meta charset="utf-8">
<title>LWR Pty Ltd – Business Card</title>
<link href="https://fonts.googleapis.com/css2?family=Open+Sans:wght@400;600;700;800&display=swap" rel="stylesheet">
<style>
  :root {
    --stage: #2b2f33;
    --black: #070707;
    --ink: #ffffff;
    --gold-light: #a88444;
    --gold-mid: #8a6a35;
    --gold-dark: #4a3519;
    --bullet: #b8914a;
    --silver: #b9bcc0;
    --frame: rgba(255,255,255,0.85);
  }
  * { box-sizing: border-box; margin: 0; padding: 0; }
  html, body { width: 1200px; height: 900px; overflow: hidden; }
  body {
    background: var(--stage);
    font-family: "Open Sans", Arial, sans-serif;
    color: var(--ink);
    display: flex;
    flex-direction: column;
    align-items: center;
    justify-content: center;
    gap: 56px;
  }
  .card {
    position: relative;
    width: 620px;
    height: 354px;
    overflow: hidden;
    background: var(--black);
    box-shadow: 0 10px 30px rgba(0,0,0,0.45);
  }
  .card-frame {
    position: absolute;
    inset: 14px;
    border: 1px solid var(--frame);
    pointer-events: none;
    z-index: 5;
  }
  .wordmark {
    font-weight: 800;
    color: var(--silver);
    letter-spacing: 2px;
    line-height: 1;
    white-space: nowrap;
  }

  /* Front */
  .front { display: flex; }
  .front-brand {
    width: 40%;
    height: 100%;
    background: radial-gradient(circle at 50% 45%, #3a3c3f 0%, #151617 55%, var(--black) 80%);
    display: flex;
    align-items: center;
    justify-content: center;
    padding-bottom: 30px;
  }
  .front-brand .wordmark { font-size: 72px; }
  .front-details {
    position: relative;
    width: 60%;
    height: 100%;
    background: linear-gradient(180deg, var(--gold-light) 0%, var(--gold-mid) 50%, var(--gold-dark) 100%);
    padding: 30px 28px 0 26px;
  }
  .company-name { font-size: 34px; font-weight: 800; line-height: 1.1; }
  .person-title { font-size: 17px; font-weight: 700; margin-top: 4px; }
  .contact-list { list-style: none; margin-top: 12px; font-size: 13px; font-weight: 600; line-height: 1.5; }
  .truck-photo {
    position: absolute;
    left: 0;
    bottom: 0;
    width: 200px;
    height: 140px;
    background: linear-gradient(120deg, #e6e6e2 0%, #b7b6b0 40%, #3d3a34 70%, #1c1a17 100%);
  }

  /* Back */
  .back .haul-photo {
    position: absolute;
    left: 0;
    bottom: 0;
    width: 100%;
    height: 48%;
    background: linear-gradient(170deg, rgba(7,7,7,1) 0%, rgba(7,7,7,0) 28%),
                linear-gradient(100deg, #c99a6a 0%, #b07e4e 40%, #6b4a2c 75%, #1a120b 100%);
  }
  .back-brand {
    position: absolute;
    left: 196px;
    top: 152px;
    z-index: 3;
  }
  .back-brand .wordmark { font-size: 80px; }
  .service-list {
    position: absolute;
    list-style: none;
    font-size: 12.5px;
    font-weight: 700;
    line-height: 1.45;
    z-index: 4;
  }
  .service-list li { display: flex; align-items: center; gap: 8px; white-space: nowrap; }
  .service-list li::before {
    content: "";
    width: 8px;
    height: 8px;
    border-radius: 50%;
    background: var(--bullet);
    flex: none;
  }
  .services-primary { left: 32px; top: 28px; }
  .services-secondary { right: 32px; top: 110px; }
</style>
</head>
<body>

  <section class="card front">
    <div class="front-brand">
      <span class="wordmark">LWR</span>
    </div>
    <div class="front-details">
      <h1 class="company-name">LWR Pty Ltd</h1>
      <p class="person-title">Daniel Corran (Director)</p>
      <ul class="contact-list">
        <li>Depot: Lot 444 excample address Australia</li>
        <li>Email: email@lwrservices.com.au</li>
        <li>Phone: 000 444 000</li>
        <li>Website: www.websiteaddress.com</li>
      </ul>
      <div class="truck-photo" role="img" aria-label="Photo of two road train prime movers"></div>
    </div>
    <div class="card-frame"></div>
  </section>

  <section class="card back">
    <div class="haul-photo" role="img" aria-label="Photo of a road train tipper on a red dirt road"></div>
    <ul class="service-list services-primary">
      <li>Over size Loads / Hot shot Loads</li>
      <li>Havy vehicle recovery services</li>
      <li>Potable water deleveries</li>
      <li>Road building &amp; Maintanance</li>
      <li>Earthworks</li>
      <li>Sand &amp; Mettle Supply Cartage</li>
    </ul>
    <div class="back-brand"><span class="wordmark">LWR</span></div>
    <ul class="service-list services-secondary">
      <li>Road train tippers</li>
      <li>Road train tankers</li>
      <li>Road train flat tops</li>
      <li>Drop deck Trailers</li>
      <li>Mine site accredited</li>
      <li>Equipments &amp; Operetors</li>
    </ul>
    <div class="card-frame"></div>
  </section>

</body>
</html>
```